need 4 creative A frame (SANDWICH BOARD) designs concepts for dental office

need 4 creative A frame (SANDWICH BOARD) designs concepts
1 - targeting kids
2. targeting old age
3. targeting teens
4 targeting general public

website - www.brenvaxdental.ca

LINK for Measurements for sandwich board https://www.korvepa.ca/BL_1921/Aluminum-Snap-Edge-A-Frame-Sign

i am attaching certain key ingredients ( rough sketch in uploaded files ) to be added on each design though not mandatory if the design is very creative

```html
<!DOCTYPE html>
<html lang="en">
<head>
<meta charset="utf-8">
<title>Brenvax Dental – A-Frame Sign</title>
<link rel="stylesheet" href="https://fonts.googleapis.com/css2?family=Libre+Baskerville:wght@400;700&family=Montserrat:wght@500;700;800&family=Oswald:wght@600&display=swap">
<style>
  :root {
    --page-bg: #ececec;
    --sign-bg: #ffffff;
    --ink: #111111;
    --brand-blue: #1fa8e6;
    --brand-blue-dark: #0f8fd0;
    --teal: #1f5a6b;
    --logo-grey: #7a7a7a;
    --white: #ffffff;
  }
  * { margin: 0; padding: 0; box-sizing: border-box; }
  html, body { width: 1200px; height: 2565px; overflow: hidden; background: var(--page-bg); }
  .sign {
    position: absolute; left: 100px; top: 645px;
    width: 1001px; height: 1275px;
    background: var(--sign-bg);
    overflow: hidden;
    box-shadow: 0 6px 18px rgba(0,0,0,.25);
  }
  .sign > * { position: absolute; }
  .kids-photo {
    left: 478px; top: 16px; width: 512px; height: 520px;
    background: linear-gradient(180deg, #f4dccb 0%, #eebf9e 45%, #d9706a 80%, #c24a4c 100%);
    border-radius: 46% 46% 0 0 / 30% 30% 0 0;
  }
  .waves { left: 0; top: 0; width: 1001px; height: 1275px; }

  .headline-block {
    left: 100px; top: 80px; width: 352px;
    font-family: "Libre Baskerville", serif; font-weight: 700; color: var(--ink);
    line-height: 1; white-space: nowrap;
  }
  .headline-block > * { display: block; }
  .headline__healthy { font-size: 58px; text-align: right; }
  .headline__smile-row {
    display: flex; align-items: baseline; gap: 12px;
    padding-left: 6px; margin-top: 6px; height: 88px;
  }
  .headline__smile { font-size: 70px; font-weight: 400; color: var(--brand-blue); }
  .headline__is { font-size: 32px; }
  .headline__cornerstone { font-size: 29px; text-align: right; margin-top: -8px; }
  .headline__age { font-size: 38px; color: var(--brand-blue); text-align: right; margin-top: 8px; }

  .badge {
    width: 208px; height: 208px; border-radius: 50%;
    background: radial-gradient(circle at 40% 35%, #39c2f5, var(--brand-blue-dark));
    border: 5px solid #bfe6f8;
    display: flex; flex-direction: column; align-items: center; justify-content: center;
    color: var(--white); font-family: "Oswald", sans-serif; font-weight: 600; text-align: center; line-height: 1.05;
  }
  .badge--open { left: 46px; top: 552px; }
  .badge--billing { left: 748px; top: 555px; }
  .badge svg { margin-bottom: 4px; }
  .badge__big { font-size: 44px; }
  .badge__mid { font-size: 34px; }
  .brand-name {
    left: 290px; top: 600px; width: 430px; text-align: center;
    font-family: "Montserrat", sans-serif; font-weight: 500; color: var(--logo-grey);
    font-size: 66px; line-height: 1.05;
  }
  .arrow { left: 0; top: 0; width: 1001px; height: 1275px; }
  .arrow-label {
    left: 290px; top: 802px; width: 528px; text-align: center;
    font-family: "Montserrat", sans-serif; font-weight: 800; font-size: 74px; color: var(--white); line-height: 1;
  }
  .patients-pill {
    left: 78px; top: 954px; width: 848px; height: 86px; border-radius: 43px;
    background: linear-gradient(180deg, #35c0f4, var(--brand-blue-dark));
    border: 3px solid #9fdcf7;
    color: var(--white); font-family: "Montserrat", sans-serif; font-weight: 800; font-size: 46px;
    display: flex; align-items: center; justify-content: center; letter-spacing: 1px;
  }
  .phone-icon { left: 164px; top: 1068px; }
  .phone-number {
    left: 265px; top: 1068px; font-family: "Montserrat", sans-serif; font-weight: 800;
    font-size: 76px; color: var(--ink); line-height: 1; white-space: nowrap;
  }
  .footer-band {
    left: 0; top: 1175px; width: 1001px; height: 100px; background: var(--teal);
    display: flex; align-items: center; justify-content: center;
    color: var(--white); font-family: "Montserrat", sans-serif; font-weight: 700; font-size: 32px; letter-spacing: 11px;
  }
</style>
</head>
<body>
  <div class="sign">
    <div class="kids-photo" role="img" aria-label="Photo of two smiling children, a girl hugging a boy from behind"></div>

    <svg class="waves" viewBox="0 0 1001 1275" aria-hidden="true">
      <defs>
        <linearGradient id="lowerFill" x1="0" y1="0" x2="0" y2="1">
          <stop offset="0" stop-color="#eaf6fd"/>
          <stop offset="0.5" stop-color="#cfeaf9"/>
          <stop offset="1" stop-color="#e9f6fd"/>
        </linearGradient>
        <linearGradient id="bandBlue" x1="0" y1="0" x2="1" y2="0">
          <stop offset="0" stop-color="#1fa8e6"/>
          <stop offset="0.5" stop-color="#38c4f6"/>
          <stop offset="1" stop-color="#1a9be0"/>
        </linearGradient>
      </defs>
      <path d="M0,470 C200,420 400,450 560,520 C720,585 880,560 1001,470 L1001,1275 L0,1275 Z" fill="url(#lowerFill)"/>
      <path d="M0,450 C200,420 400,440 560,510 C720,575 880,545 1001,455 L1001,480 C880,575 720,600 560,545 C400,480 200,455 0,520 Z" fill="#c9cdd1"/>
      <path d="M0,380 C200,340 420,370 570,450 C720,520 880,500 1001,375 L1001,455 C880,545 720,565 560,505 C400,440 200,420 0,450 Z" fill="url(#bandBlue)"/>
      <path d="M0,520 C60,500 90,540 0,660 Z" fill="#1fa8e6" opacity=".85"/>
      <path d="M640,1060 C780,960 900,880 1001,820" stroke="#ffffff" stroke-width="6" fill="none" opacity=".7"/>
    </svg>

    <div class="headline-block">
      <span class="headline__healthy">HEALTHY</span>
      <span class="headline__smile-row">
        <span class="headline__smile">Smile</span>
        <span class="headline__is">IS</span>
      </span>
      <span class="headline__cornerstone">CORNERSTONE</span>
      <span class="headline__age">OF EVERY AGE</span>
    </div>

    <div class="badge badge--open">
      <svg width="110" height="70" viewBox="0 0 110 70" aria-hidden="true">
        <path d="M40,22 L55,6 L70,22" stroke="#fff" stroke-width="4" fill="none"/>
        <circle cx="55" cy="6" r="4" fill="#fff"/>
        <rect x="6" y="22" width="98" height="44" rx="4" fill="none" stroke="#fff" stroke-width="4"/>
        <text x="55" y="56" text-anchor="middle" fill="#fff" font-family="Oswald, sans-serif" font-weight="600" font-size="32">OPEN</text>
      </svg>
      <span class="badge__big">7 DAYS</span>
    </div>

    <div class="brand-name">Brenvax<br>Dental</div>

    <div class="badge badge--billing">
      <svg width="64" height="64" viewBox="0 0 64 64" aria-hidden="true">
        <rect x="18" y="6" width="36" height="48" rx="3" fill="none" stroke="#fff" stroke-width="3"/>
        <line x1="26" y1="22" x2="46" y2="22" stroke="#fff" stroke-width="3"/>
        <line x1="26" y1="32" x2="46" y2="32" stroke="#fff" stroke-width="3"/>
        <line x1="26" y1="42" x2="40" y2="42" stroke="#fff" stroke-width="3"/>
        <path d="M4,30 L14,30 M2,38 L14,38" stroke="#fff" stroke-width="3"/>
      </svg>
      <span class="badge__mid">WE DIRECT<br>BILL</span>
    </div>

    <svg class="arrow" viewBox="0 0 1001 1275" aria-hidden="true">
      <polygon points="185,844 281,765 281,800 818,800 818,885 281,885 281,922" fill="var(--teal)"/>
    </svg>
    <div class="arrow-label">WE ARE IN</div>

    <div class="patients-pill">ACCEPTING NEW PATIENTS</div>

    <svg class="phone-icon" width="76" height="76" viewBox="0 0 76 76" aria-hidden="true">
      <circle cx="38" cy="38" r="37" fill="var(--teal)"/>
      <path d="M26,20 C22,22 20,26 22,32 C26,44 34,52 46,56 C52,58 56,55 58,51 L50,44 C48,46 46,47 44,46 C38,43 34,39 31,33 C30,31 31,29 33,27 Z" fill="none" stroke="#fff" stroke-width="3" stroke-linejoin="round"/>
      <path d="M42,22 A14,14 0 0 1 56,36 M42,14 A22,22 0 0 1 64,36" fill="none" stroke="#fff" stroke-width="3"/>
    </svg>
    <div class="phone-number">(587) 555-0148</div>

    <div class="footer-band">www.BrenvaxDental.ca</div>
  </div>
</body>
</html>
```